Business Card for Jewelry Business

We need a new namecard design for a jewelry company based in Bangkok, Thailand. We have a new website recently and want the new namecard to reflect our new modern image. I have uploaded our old namecard to show you the information that needs to be on the namecard. Pls check our website www.qelnotrax.com for the new color scheme to help design the new namecard.

```html
<!DOCTYPE html>
<html lang="en">
<head>
<meta charset="utf-8">
<title>Qelnotrax Business Card</title>
<link rel="stylesheet" href="https://fonts.googleapis.com/css2?family=Montserrat:wght@400;500;700&display=swap">
<style>
  :root {
    --bg: #2b2b2b;
    --card-white: #ffffff;
    --card-dark: #242424;
    --teal: #4fbcc6;
    --ink: #222222;
    --muted: #3a3a3a;
  }
  html, body {
    margin: 0;
    padding: 0;
    width: 1200px;
    height: 1186px;
    overflow: hidden;
    background: var(--bg);
    font-family: "Montserrat", sans-serif;
  }
  .stage {
    position: relative;
    width: 1200px;
    height: 1186px;
  }
  .card {
    position: absolute;
    left: 220px;
    width: 760px;
    height: 434px;
    border-radius: 26px;
    overflow: hidden;
    box-sizing: border-box;
  }
  .card-back {
    top: 128px;
    background: var(--card-dark);
  }
  .back-pattern {
    position: absolute;
    inset: 0;
    background: linear-gradient(110deg, #6a6a6a 0%, #3a3a3a 35%, #222222 70%, #1c1c1c 100%);
  }
  .back-mark {
    position: absolute;
    right: 40px;
    bottom: 34px;
    color: var(--teal);
    font-weight: 700;
    font-size: 14px;
    letter-spacing: 2px;
  }
  .card-front {
    top: 612px;
    background: var(--card-white);
    padding: 52px 56px;
  }
  .person-name {
    margin: 0;
    color: var(--teal);
    font-weight: 700;
    font-size: 30px;
    line-height: 1.1;
  }
  .person-title {
    margin: 4px 0 18px;
    color: var(--muted);
    font-size: 16px;
  }
  .company-name {
    margin: 0 0 4px;
    color: var(--teal);
    font-weight: 700;
    font-size: 17px;
  }
  .address {
    margin: 0 0 28px;
    color: var(--ink);
    font-size: 16px;
    line-height: 1.3;
  }
  .contact-list {
    list-style: none;
    margin: 0;
    padding: 0;
  }
  .contact-list li {
    display: flex;
    align-items: center;
    gap: 12px;
    color: var(--ink);
    font-size: 16px;
    line-height: 24px;
  }
  .contact-list svg {
    width: 14px;
    height: 14px;
    flex: none;
  }
  .brand {
    position: absolute;
    right: 60px;
    top: 150px;
    display: flex;
    align-items: center;
    gap: 14px;
  }
  .brand-dot {
    width: 22px;
    height: 22px;
    border-radius: 50%;
    background: var(--teal);
  }
  .brand-name {
    color: var(--ink);
    font-weight: 500;
    font-size: 30px;
    letter-spacing: 3px;
  }
</style>
</head>
<body>
<main class="stage">
  <section class="card card-back">
    <div class="back-pattern" role="img" aria-label="Repeating monogram pattern in silver and black gloss"></div>
    <span class="back-mark">QELNOTRAX</span>
  </section>

  <section class="card card-front">
    <h1 class="person-name">Naree Sombat</h1>
    <p class="person-title">Sales &amp; Product Development Manager</p>
    <p class="company-name">Qelnotrax Jewelry Co. Ltd</p>
    <p class="address">218 Moo 7, Trade Processing Zone 2<br>Sai Thong Industrial Park,<br>Bangkok, 10990 thailand</p>
    <ul class="contact-list">
      <li><svg viewBox="0 0 14 14"><path fill="#4fbcc6" d="M3 1h2l1 3-1.5 1a7 7 0 0 0 4.5 4.5L10 8l3 1v2a2 2 0 0 1-2 2A10 10 0 0 1 1 3a2 2 0 0 1 2-2z"/></svg>662-418-0273</li>
      <li><svg viewBox="0 0 14 14"><rect x="3" y="0.5" width="8" height="13" rx="1.5" fill="#4fbcc6"/><rect x="4.5" y="2" width="5" height="8" fill="#fff"/></svg>662-590-3164</li>
      <li><svg viewBox="0 0 14 14"><rect x="0.5" y="2.5" width="13" height="9" rx="1" fill="#4fbcc6"/><path d="M1 3l6 5 6-5" stroke="#fff" fill="none"/></svg>naree@qelnotrax.com</li>
      <li><svg viewBox="0 0 14 14"><rect x="0.5" y="2.5" width="13" height="9" rx="1" fill="#4fbcc6"/><path d="M1 3l6 5 6-5" stroke="#fff" fill="none"/></svg>hello@qelnotrax.com</li>
      <li><svg viewBox="0 0 14 14"><circle cx="7" cy="7" r="6.5" fill="#4fbcc6"/><path d="M0.5 7h13M7 0.5c-3 3-3 10 0 13M7 0.5c3 3 3 10 0 13" stroke="#fff" fill="none" stroke-width="0.8"/></svg>www.qelnotrax.com</li>
      <li><svg viewBox="0 0 14 14"><circle cx="7" cy="7" r="6.5" fill="#4fbcc6"/></svg>@qelnotrax studio</li>
      <li><svg viewBox="0 0 14 14"><circle cx="7" cy="7" r="6.5" fill="#4fbcc6"/></svg>@qelnotrax</li>
    </ul>
    <div class="brand">
      <span class="brand-dot"></span>
      <span class="brand-name">QELNOTRAX</span>
    </div>
  </section>
</main>
</body>
</html>
```